Business Card Design for Occupational Medicine Start Up Company

We need to design a professional business card. We are a healthcare company providing occupational medicine services to blue collar industries. We are professional, efficient and high quality service providers.

Target Market(s)

Blue Collar Industry: Shipbuilding, Ports, Trucking Companies; The Executives and Safety Officers for these companies

Industry/Entity Type

Healthcare

Contact Information for Business Card

Logo, Name, Title, Email, Phone

Other font styles liked:
• Please match our Brand Guide

Requirements
Must have
• Our Company Colors and Logo

```html
<!DOCTYPE html>
<html lang="en">
<head>
<meta charset="utf-8">
<title>Crewline Health — Business Card</title>
<link href="https://fonts.googleapis.com/css2?family=Montserrat:wght@400;500;600;700&display=swap" rel="stylesheet">
<style>
  :root {
    --stage: #e4e4e6;
    --card-light: #ececed;
    --navy: #2b2d80;
    --navy-back: #2e3186;
    --orange: #f4a73a;
    --blue: #2f97dc;
    --sky: #6cc3ee;
    --ink-soft: #5d6068;
    --white: #ffffff;
  }
  * { margin: 0; padding: 0; box-sizing: border-box; }
  html, body { width: 1200px; height: 1107px; overflow: hidden; }
  body {
    background: var(--stage);
    font-family: "Montserrat", Arial, sans-serif;
    position: relative;
  }
  .card {
    position: absolute;
    left: 180px;
    width: 840px;
    height: 483px;
    box-shadow: 0 6px 18px rgba(0,0,0,0.18);
  }
  .card-front { top: 44px; background: var(--card-light); }
  .card-back  { top: 580px; background: var(--navy-back); }

  .holder { position: absolute; left: 61px; top: 50px; }
  .holder-name { font-size: 27px; font-weight: 500; color: var(--navy); letter-spacing: 0.2px; }
  .holder-name .surname { color: var(--orange); }
  .holder-title { font-size: 16px; color: var(--ink-soft); margin-top: 6px; }

  .accent-bars { position: absolute; left: 26px; top: 258px; display: flex; gap: 3px; }
  .accent-bars span { display: block; width: 4px; height: 78px; }
  .accent-bars .bar-orange { background: var(--orange); }
  .accent-bars .bar-blue { background: var(--blue); }
  .accent-bars .bar-sky { background: var(--sky); }

  .contacts { position: absolute; left: 61px; top: 254px; list-style: none; }
  .contacts li {
    display: flex; align-items: center; gap: 12px;
    font-size: 18px; color: var(--ink-soft); height: 28px;
  }
  .contacts svg { width: 15px; height: 15px; flex: none; }
  .contacts .web-accent { color: var(--orange); }

  .address { position: absolute; left: 61px; top: 354px; font-size: 18px; line-height: 30px; color: var(--ink-soft); }

  .front-brand {
    position: absolute; left: 520px; top: 222px;
    display: flex; align-items: center; gap: 12px;
    font-size: 28px; font-weight: 600; color: var(--navy);
  }
  .front-brand .dot { width: 22px; height: 22px; border-radius: 50%; background: var(--orange); }

  .back-brand {
    position: absolute; left: 0; right: 0; top: 200px;
    display: flex; justify-content: center; align-items: center; gap: 16px;
    font-size: 44px; font-weight: 600; color: var(--white); letter-spacing: 1px;
  }
  .back-brand .dot { width: 30px; height: 30px; border-radius: 50%; background: var(--white); }
  .back-corner {
    position: absolute; right: 50px; bottom: 42px;
    font-size: 14px; font-weight: 600; color: var(--white); letter-spacing: 0.5px;
  }
</style>
</head>
<body>
  <section class="card card-front">
    <div class="holder">
      <div class="holder-name">Nadia <span class="surname">Berrada</span></div>
      <div class="holder-title">Directeur</div>
    </div>

    <div class="accent-bars"><span class="bar-sky"></span><span class="bar-orange"></span><span class="bar-blue"></span></div>

    <ul class="contacts">
      <li>
        <svg viewBox="0 0 16 16" aria-hidden="true"><path fill="var(--navy)" d="M3.6 1.5l2.3 2.6-1.3 1.6c.9 2 2.6 3.7 4.6 4.7l1.6-1.3 2.6 2.3-1.5 2.2C6.8 13.4 2.6 9.2 1.4 3.1z"/></svg>
        +0212 0600 482 130
      </li>
      <li>
        <svg viewBox="0 0 16 16" aria-hidden="true"><rect x="1" y="3" width="14" height="10" rx="1" fill="var(--navy)"/><path d="M1.5 3.8L8 8.8l6.5-5" stroke="var(--card-light)" stroke-width="1.3" fill="none"/></svg>
        n.berrada@crewline.ma
      </li>
      <li>
        <svg viewBox="0 0 16 16" aria-hidden="true"><circle cx="8" cy="8" r="6.5" fill="var(--navy)"/><path d="M1.5 8h13M8 1.5c-3 3.5-3 9.5 0 13M8 1.5c3 3.5 3 9.5 0 13" stroke="var(--card-light)" stroke-width="1" fill="none"/></svg>
        <span>www.<span class="web-accent">crewlinehealth</span>.ma</span>
      </li>
    </ul>

    <div class="address">PO BOX 50312 Millgate<br>Calgary, AB T3K-4R</div>

    <div class="front-brand"><span class="dot"></span>Crewline Health</div>
  </section>

  <section class="card card-back">
    <div class="back-brand"><span class="dot"></span>CREWLINE HEALTH</div>
    <div class="back-corner">CREWLINE</div>
  </section>
</body>
</html>
```